Small Ecommerce Styled Site to Sell / Lease Domain Names

We have a small portfolio of 100+ domain names that we would like to offer for sale or lease via a web site. Along the lines of http://www.velramarkets.com/searchdomain.html?priceChoice=2&sort=leasing_desc

We would like initially a 4 page design, listing page (as site referenced above), domain info page (Universal Domain Name Landing Page with form) and checkout a page and About Us Page

We do not want a replica of the site listed, please use it as a guide only, we are looking for a fresh design, in similar concept web 2.0

Our Colours are #351a41 (Main) - #ffca27 (Secondary) all other colours must compliment those 2.
Updates

Domain Landing Page:  I am sorry I was not clear about expectations, however we would like a domain landing page that would be the default holding page for a domain name.

For some examples of what I mean please see:
https://www.pobexhub.com.au/guest-articles/7626-domain-for-sale-landing-pages.html
http://dev.quillterbrokers.com/blog/2013/09/sales-only-landers-and-buy-it-now-2/

Industry/Entity Type

Domain

Font styles to use
Sans Serif

```html
<!DOCTYPE html>
<html lang="en">
<head>
<meta charset="utf-8">
<title>YourDomainName.com – Domains For Sale</title>
<link href="https://fonts.googleapis.com/css2?family=Ubuntu:wght@400;500;700&display=swap" rel="stylesheet">
<style>
:root{
  --main:#351a41;
  --main-deep:#2a1434;
  --main-soft:#4a2a5a;
  --accent:#ffca27;
  --accent-dark:#e0a800;
  --row-alt:#f6f0f9;
  --row-head:#dccbe6;
  --line:#e6c96a;
  --muted:#555;
  --text:#333;
  --blue:#3a9be8;
  --field:#eef0d8;
  --white:#fff;
}
*{box-sizing:border-box;margin:0;padding:0}
html,body{width:1200px;height:2632px;overflow:hidden}
body{font-family:"Ubuntu",sans-serif;color:var(--text);background:var(--white);position:relative;font-size:17px}
a{color:inherit;text-decoration:none}
svg.ic{width:18px;height:18px;display:inline-block;vertical-align:middle}

/* top bar */
.topbar{position:absolute;top:0;left:0;width:1200px;height:46px;background:var(--main-deep);display:flex;justify-content:flex-end}
.topbar a{color:#fff;font-size:16px;display:flex;align-items:center;gap:7px;padding:0 18px;border-left:1px solid #4a2f56}
.topbar svg{stroke:var(--accent);fill:none;stroke-width:2}

/* hero */
.hero{position:absolute;top:46px;left:0;width:1200px;height:331px;background:radial-gradient(ellipse at 50% 40%,#9a86a6 0%,#6d5579 45%,#3f2449 100%);text-align:center}
.hero-title{position:absolute;top:76px;left:0;right:0}
.hero-title .sale{color:var(--accent);font-size:44px;font-weight:500;display:block;line-height:1}
.hero-title h1{color:#fff;font-size:72px;font-weight:500;line-height:1.1;margin-top:6px}
.hero-band{position:absolute;left:0;bottom:0;width:1200px;height:10px;background:var(--main)}
.mainnav{position:absolute;top:365px;left:284px;width:658px;height:44px;background:var(--accent);border:1px solid var(--accent-dark);border-radius:3px;display:flex}
.mainnav a{flex:1;display:flex;align-items:center;justify-content:center;font-size:20px;color:var(--main);border-right:1px solid var(--accent-dark)}
.mainnav a:last-child{border-right:0}

/* sidebar */
.sidebar{position:absolute;left:25px;top:451px;width:270px}
.panel{border:1px solid #ddd;box-shadow:0 1px 3px rgba(0,0,0,.12);background:#fff;position:absolute;left:0;width:270px}
.panel h3{background:var(--main);color:#fff;font-weight:500;font-size:20px;height:40px;line-height:40px;padding-left:14px;position:relative}
.panel h3::after{content:"";position:absolute;right:-1px;top:0;border-style:solid;border-width:0 14px 14px 0;border-color:transparent #fff transparent transparent}
.cats li{list-style:none;height:44.5px;display:flex;align-items:center;gap:8px;padding-left:6px;border-bottom:1px solid #e3e3e3;font-size:16.5px;color:#333}
.cats .plus{width:15px;height:15px;border-radius:50%;background:var(--main);position:relative;flex:none}
.cats .plus::before,.cats .plus::after{content:"";position:absolute;background:#fff;left:3.5px;top:6.5px;width:8px;height:2px}
.cats .plus::after{transform:rotate(90deg)}
.cats .active{background:#ececec;border-left:5px solid var(--accent);padding-left:26px}
.cats .sub{padding-left:54px;border-bottom:0}
.cats .sub.on{color:var(--accent-dark)}
.box{width:17px;height:17px;background:var(--field);border:1px solid #c8c8b4;flex:none;display:inline-block}
.checks{display:grid;grid-template-columns:repeat(3,1fr);row-gap:22px;padding:16px 10px 14px}
.checks label,.lang label{display:flex;align-items:center;gap:10px;font-size:16px}
.range{display:flex;align-items:center;justify-content:space-between;padding:20px 12px 20px 10px;font-size:16px}
.range .field{width:72px;height:26px;background:var(--field);border:1px solid #c8c8b4;color:#999;text-align:center;line-height:24px;margin-left:6px}
.range span{display:flex;align-items:center}
.ws{padding:14px 14px 10px}
.ws .row{display:flex;align-items:center;justify-content:space-between;height:44px;font-size:16px}
.ws .field{width:136px;height:28px;background:var(--field);border:1px solid #c8c8b4}
.ws label{display:flex;align-items:center;gap:10px;font-size:15px;height:30px;padding-left:4px}
.lang{display:grid;grid-template-columns:1fr 1fr;row-gap:17px;padding:16px 10px 14px}
.btn-search{position:absolute;left:0;top:1828px;width:270px;height:51px;background:var(--accent);border:1px solid var(--accent-dark);color:var(--main);font-size:28px;text-align:center;line-height:49px;border-radius:2px}

/* main */
.search{position:absolute;left:807px;top:453px;width:366px;height:38px;display:flex;border:1px solid #ddd}
.search .q{flex:1;display:flex;align-items:center;gap:10px;padding-left:10px;color:#999;font-size:16px}
.search .q svg{stroke:var(--main);fill:none;stroke-width:2.5}
.search .go{width:80px;background:var(--main);color:var(--accent);font-size:18px;display:flex;align-items:center;justify-content:center}
.tabs{position:absolute;left:339px;top:519px;display:flex;gap:6px}
.tabs a{height:46px;display:flex;align-items:center;justify-content:center;font-size:24px;background:var(--accent);color:var(--main)}
.tabs .on{background:var(--main);color:var(--accent)}
.listing{position:absolute;left:339px;top:565px;width:836px;border-top:9px solid var(--main);border-collapse:collapse}
.listing th{background:var(--row-head);height:40px;font-weight:400;font-size:17px;text-align:left;color:#333}
.listing td{height:56px;border-bottom:1px solid var(--line);font-size:16.5px;color:#333}
.listing tbody tr:nth-child(even){background:var(--row-alt)}
.c-name{padding-left:21px;width:320px}
.c-cat{width:290px;white-space:nowrap}
.c-cat svg{stroke:#333;fill:none;stroke-width:1.6;margin-right:8px}
.c-fee{width:110px}
.fee{display:inline-flex;align-items:center;gap:6px;background:var(--accent);border:1px solid var(--accent-dark);border-radius:4px;height:31px;width:91px;padding-left:7px;font-size:16px;color:var(--main)}
.fee svg{stroke:var(--main);fill:none;stroke-width:1.6}
.offer{display:inline-flex;align-items:center;gap:6px;background:var(--main);border:1px solid #1e0e26;border-radius:4px;height:31px;width:119px;padding-left:8px;font-size:15.5px;color:var(--accent)}
.offer svg{stroke:var(--accent);fill:none;stroke-width:1.6}
.buy{display:inline-flex;align-items:center;gap:14px;background:var(--blue);border:1px solid #2a7ec4;border-radius:4px;height:31px;width:119px;padding-left:9px;font-size:16px;color:#fff}
.buy svg{stroke:#fff;fill:none;stroke-width:1.8}
.pager{position:absolute;top:2223px;right:25px;display:flex;gap:5px;align-items:center}
.pager a{min-width:30px;height:28px;border:1px solid #bbb;border-radius:3px;background:#f3f3f3;font-size:14px;display:flex;align-items:center;justify-content:center;padding:0 4px;color:#444}
.pager .on{background:var(--main);color:#fff;border-color:var(--main)}
.pager .gap{border:0;background:none;min-width:16px}

/* footer */
.footer{position:absolute;left:0;top:2373px;width:1200px;height:192px;background:var(--main);border-top:3px solid var(--accent);display:flex;color:#fff}
.footer .col{padding:28px 25px 0}
.footer .col + .col{border-left:1px solid #5a3a68}
.footer h4{font-size:22px;font-weight:400;margin-bottom:20px}
.footer p{font-size:15px;line-height:1.3;color:#e3d8e8}
.footer li{list-style:none;font-size:16px;color:#e3d8e8;margin-bottom:14px;display:flex;align-items:center;gap:12px}
.footer li::before{content:"›";color:var(--accent);font-size:20px;line-height:0}
.social{display:flex;gap:9px}
.social span{width:43px;height:43px;background:var(--accent)}
.copy{position:absolute;left:25px;top:2590px;font-size:15px;color:#333}
</style>
</head>
<body>
<svg width="0" height="0" style="position:absolute" aria-hidden="true">
  <defs>
    <symbol id="i-user" viewBox="0 0 20 20"><circle cx="10" cy="7" r="4"/><path d="M3 18c1-4 4-6 7-6s6 2 7 6z"/></symbol>
    <symbol id="i-cart" viewBox="0 0 20 20"><path d="M1 3h3l2 10h11l2-7H5"/><circle cx="8" cy="17" r="1.3"/><circle cx="15" cy="17" r="1.3"/></symbol>
    <symbol id="i-help" viewBox="0 0 20 20"><circle cx="10" cy="10" r="8"/><path d="M7.5 8a2.5 2.5 0 1 1 3.5 2.3c-.8.4-1 1-1 1.7"/><path d="M10 14.5v.5"/></symbol>
    <symbol id="i-laptop" viewBox="0 0 20 20"><rect x="4" y="4" width="12" height="9"/><path d="M1 16h18"/></symbol>
    <symbol id="i-coins" viewBox="0 0 20 20"><ellipse cx="10" cy="5" rx="6" ry="2.2"/><path d="M4 5v3c0 1.2 2.7 2.2 6 2.2s6-1 6-2.2V5"/><path d="M4 10.5v3c0 1.2 2.7 2.2 6 2.2s6-1 6-2.2v-3"/><path d="M2 12h4M14 8h4"/></symbol>
    <symbol id="i-tag" viewBox="0 0 20 20"><path d="M2 10l8-8h7v7l-8 8z"/><circle cx="13.5" cy="6.5" r="1.3"/></symbol>
    <symbol id="i-search" viewBox="0 0 20 20"><circle cx="8" cy="8" r="5.5"/><path d="M12 12l6 6"/></symbol>
  </defs>
</svg>

<nav class="topbar">
  <a href="#"><svg class="ic"><use href="#i-user"/></svg>Signup</a>
  <a href="#"><svg class="ic"><use href="#i-user"/></svg>Login</a>
  <a href="#"><svg class="ic"><use href="#i-cart"/></svg>Cart</a>
  <a href="#"><svg class="ic"><use href="#i-help"/></svg>FAQ</a>
</nav>

<header class="hero" role="img" aria-label="Scattered grey cubes labelled with domain extensions on a purple background">
  <div class="hero-title">
    <span class="sale">For Sale</span>
    <h1>YourDomainName.com</h1>
  </div>
  <div class="hero-band"></div>
</header>
<nav class="mainnav">
  <a href="#">Buy Domains</a><a href="#">Lease Domains</a><a href="#">Categories</a><a href="#">About Us</a>
</nav>

<aside class="sidebar">
  <section class="panel" style="top:0">
    <h3>Categories</h3>
    <ul class="cats">
      <li><span class="plus"></span>Automotive</li>
      <li class="active">Business and Finance</li>
      <li class="sub">Women's Apparel</li>
      <li class="sub on">Dresses</li>
      <li class="sub">Tops &amp; Blouses</li>
      <li class="sub">T-Shirts</li>
      <li><span class="plus"></span>Computers and Internet</li>
      <li><span class="plus"></span>Education</li>
      <li><span class="plus"></span>Entertainment</li>
      <li><span class="plus"></span>Family</li>
      <li><span class="plus"></span>Food and Beverage</li>
      <li><span class="plus"></span>Food and Beverage</li>
      <li><span class="plus"></span>Food and Beverage</li>
      <li style="border-bottom:0"><span class="plus"></span>Food and Beverage</li>
    </ul>
  </section>

  <section class="panel" style="top:696px">
    <h3>Extensions</h3>
    <div class="checks">
      <label><i class="box"></i>All</label><label><i class="box"></i>.com</label><label><i class="box"></i>.net</label>
      <label><i class="box"></i>.info</label><label><i class="box"></i>.org</label><label><i class="box"></i>.co.uk</label>
      <label><i class="box"></i>.co.za</label><label><i class="box"></i>.es</label><label><i class="box"></i>.de</label>
    </div>
  </section>

  <section class="panel" style="top:914px">
    <h3>Price Range</h3>
    <div class="range"><span>Min:<i class="field">0</i></span><span>Max:<i class="field">0</i></span></div>
  </section>

  <section class="panel" style="top:1043px">
    <h3>Length</h3>
    <div class="range"><span>Min:<i class="field">0</i></span><span>Max:<i class="field">0</i></span></div>
  </section>

  <section class="panel" style="top:1177px">
    <h3>Word Count</h3>
    <div class="range"><span>Min:<i class="field">0</i></span><span>Max:<i class="field">0</i></span></div>
  </section>

  <section class="panel" style="top:1309px">
    <h3>Word Structure</h3>
    <div class="ws">
      <div class="row">Begins With:<i class="field"></i></div>
      <div class="row">Ends With:<i class="field"></i></div>
      <div class="row">Exclude:<i class="field"></i></div>
      <label><i class="box"></i>Disallow Hyphen</label>
      <label><i class="box"></i>Disallow Hyphen</label>
    </div>
  </section>

  <section class="panel" style="top:1601px">
    <h3>Language</h3>
    <div class="lang">
      <label><i class="box"></i>All</label><label><i class="box"></i>English</label>
      <label><i class="box"></i>Spanish</label><label><i class="box"></i>German</label>
      <label><i class="box"></i>French</label><label><i class="box"></i>Turkish</label>
      <label><i class="box"></i>Italian</label><label><i class="box"></i>Dutch</label>
    </div>
  </section>

  <a class="btn-search" href="#">SEARCH</a>
</aside>

<main>
  <div class="search">
    <div class="q"><svg class="ic"><use href="#i-search"/></svg>Enter Keyword or Domain</div>
    <a class="go" href="#">Search</a>
  </div>
  <div class="tabs">
    <a class="on" href="#" style="width:247px">Premium Domains</a>
    <a href="#" style="width:219px">Lease Domains</a>
    <a href="#" style="width:186px">Buy Domains</a>
  </div>

  <table class="listing">
    <thead><tr><th class="c-name">Domain Name</th><th class="c-cat" style="padding-left:90px">Category</th><th class="c-fee" style="padding-left:12px">Lease Fee</th><th style="padding-left:30px">Price</th></tr></thead>
    <tbody>
      <tr><td class="c-name">FrostNook.com</td><td class="c-cat"><svg class="ic"><use href="#i-laptop"/></svg>Computers and Internet</td><td class="c-fee"><span class="fee"><svg class="ic"><use href="#i-coins"/></svg>$240</span></td><td><span class="offer"><svg class="ic"><use href="#i-tag"/></svg>Make Offer</span></td></tr>
      <tr><td class="c-name">DesertGulfs.com</td><td class="c-cat"><svg class="ic"><use href="#i-laptop"/></svg>Computers and Internet</td><td class="c-fee"><span class="fee"><svg class="ic"><use href="#i-coins"/></svg>$1240</span></td><td><span class="offer"><svg class="ic"><use href="#i-tag"/></svg>Make Offer</span></td></tr>
      <tr><td class="c-name">DesertGulfs.com</td><td class="c-cat"><svg class="ic"><use href="#i-laptop"/></svg>Computers and Internet</td><td class="c-fee"><span class="fee"><svg class="ic"><use href="#i-coins"/></svg>$1240</span></td><td><span class="offer"><svg class="ic"><use href="#i-tag"/></svg>Make Offer</span></td></tr>
      <tr><td class="c-name">DesertGulfs.com</td><td class="c-cat"><svg class="ic"><use href="#i-laptop"/></svg>Computers and Internet</td><td class="c-fee"></td><td><span class="buy"><svg class="ic"><use href="#i-cart"/></svg>$4,288</span></td></tr>
      <tr><td class="c-name">DesertGulfs.com</td><td class="c-cat"><svg class="ic"><use href="#i-laptop"/></svg>Computers and Internet</td><td class="c-fee"><span class="fee"><svg class="ic"><use href="#i-coins"/></svg>$1240</span></td><td><span class="offer"><svg class="ic"><use href="#i-tag"/></svg>Make Offer</span></td></tr>
      <tr><td class="c-name">DesertGulfs.com</td><td class="c-cat"><svg class="ic"><use href="#i-laptop"/></svg>Computers and Internet</td><td class="c-fee"><span class="fee"><svg class="ic"><use href="#i-coins"/></svg>$1240</span></td><td><span class="offer"><svg class="ic"><use href="#i-tag"/></svg>Make Offer</span></td></tr>
      <tr><td class="c-name">DesertGulfs.com</td><td class="c-cat"><svg class="ic"><use href="#i-laptop"/></svg>Computers and Internet</td><td class="c-fee"><span class="fee"><svg class="ic"><use href="#i-coins"/></svg>$1240</span></td><td><span class="offer"><svg class="ic"><use href="#i-tag"/></svg>Make Offer</span></td></tr>
      <tr><td class="c-name">DesertGulfs.com</td><td class="c-cat"><svg class="ic"><use href="#i-laptop"/></svg>Computers and Internet</td><td class="c-fee"><span class="fee"><svg class="ic"><use href="#i-coins"/></svg>$1240</span></td><td><span class="offer"><svg class="ic"><use href="#i-tag"/></svg>Make Offer</span></td></tr>
      <tr><td class="c-name">DesertGulfs.com</td><td class="c-cat"><svg class="ic"><use href="#i-laptop"/></svg>Computers and Internet</td><td class="c-fee"><span class="fee"><svg class="ic"><use href="#i-coins"/></svg>$1240</span></td><td><span class="offer"><svg class="ic"><use href="#i-tag"/></svg>Make Offer</span></td></tr>
      <tr><td class="c-name">DesertGulfs.com</td><td class="c-cat"><svg class="ic"><use href="#i-laptop"/></svg>Computers and Internet</td><td class="c-fee"><span class="fee"><svg class="ic"><use href="#i-coins"/></svg>$1240</span></td><td><span class="offer"><svg class="ic"><use href="#i-tag"/></svg>Make Offer</span></td></tr>
      <tr><td class="c-name">FrostNook.com</td><td class="c-cat"><svg class="ic"><use href="#i-laptop"/></svg>Computers and Internet</td><td class="c-fee"><span class="fee"><svg class="ic"><use href="#i-coins"/></svg>$240</span></td><td><span class="offer"><svg class="ic"><use href="#i-tag"/></svg>Make Offer</span></td></tr>
      <tr><td class="c-name">DesertGulfs.com</td><td class="c-cat"><svg class="ic"><use href="#i-laptop"/></svg>Computers and Internet</td><td class="c-fee"><span class="fee"><svg class="ic"><use href="#i-coins"/></svg>$1240</span></td><td><span class="offer"><svg class="ic"><use href="#i-tag"/></svg>Make Offer</span></td></tr>
      <tr><td class="c-name">DesertGulfs.com</td><td class="c-cat"><svg class="ic"><use href="#i-laptop"/></svg>Computers and Internet</td><td class="c-fee"></td><td><span class="buy"><svg class="ic"><use href="#i-cart"/></svg>$5,288</span></td></tr>
      <tr><td class="c-name">DesertGulfs.com</td><td class="c-cat"><svg class="ic"><use href="#i-laptop"/></svg>Computers and Internet</td><td class="c-fee"><span class="fee"><svg class="ic"><use href="#i-coins"/></svg>$1240</span></td><td><span class="offer"><svg class="ic"><use href="#i-tag"/></svg>Make Offer</span></td></tr>
      <tr><td class="c-name">DesertGulfs.com</td><td class="c-cat"><svg class="ic"><use href="#i-laptop"/></svg>Computers and Internet</td><td class="c-fee"><span class="fee"><svg class="ic"><use href="#i-coins"/></svg>$1240</span></td><td><span class="offer"><svg class="ic"><use href="#i-tag"/></svg>Make Offer</span></td></tr>
      <tr><td class="c-name">DesertGulfs.com</td><td class="c-cat"><svg class="ic"><use href="#i-laptop"/></svg>Computers and Internet</td><td class="c-fee"><span class="fee"><svg class="ic"><use href="#i-coins"/></svg>$1240</span></td><td><span class="offer"><svg class="ic"><use href="#i-tag"/></svg>Make Offer</span></td></tr>
      <tr><td class="c-name">DesertGulfs.com</td><td class="c-cat"><svg class="ic"><use href="#i-laptop"/></svg>Computers and Internet</td><td class="c-fee"><span class="fee"><svg class="ic"><use href="#i-coins"/></svg>$1240</span></td><td><span class="offer"><svg class="ic"><use href="#i-tag"/></svg>Make Offer</span></td></tr>
      <tr><td class="c-name">DesertGulfs.com</td><td class="c-cat"><svg class="ic"><use href="#i-laptop"/></svg>Computers and Internet</td><td class="c-fee"></td><td><span class="buy"><svg class="ic"><use href="#i-cart"/></svg>$3,482</span></td></tr>
      <tr><td class="c-name">DesertGulfs.com</td><td class="c-cat"><svg class="ic"><use href="#i-laptop"/></svg>Computers and Internet</td><td class="c-fee"><span class="fee"><svg class="ic"><use href="#i-coins"/></svg>$1240</span></td><td><span class="offer"><svg class="ic"><use href="#i-tag"/></svg>Make Offer</span></td></tr>
      <tr><td class="c-name">DesertGulfs.com</td><td class="c-cat"><svg class="ic"><use href="#i-laptop"/></svg>Computers and Internet</td><td class="c-fee"><span class="fee"><svg class="ic"><use href="#i-coins"/></svg>$1240</span></td><td><span class="offer"><svg class="ic"><use href="#i-tag"/></svg>Make Offer</span></td></tr>
      <tr><td class="c-name">DesertGulfs.com</td><td class="c-cat"><svg class="ic"><use href="#i-laptop"/></svg>Computers and Internet</td><td class="c-fee"><span class="fee"><svg class="ic"><use href="#i-coins"/></svg>$1240</span></td><td><span class="offer"><svg class="ic"><use href="#i-tag"/></svg>Make Offer</span></td></tr>
      <tr><td class="c-name">DesertGulfs.com</td><td class="c-cat"><svg class="ic"><use href="#i-laptop"/></svg>Computers and Internet</td><td class="c-fee"><span class="fee"><svg class="ic"><use href="#i-coins"/></svg>$1240</span></td><td><span class="offer"><svg class="ic"><use href="#i-tag"/></svg>Make Offer</span></td></tr>
      <tr><td class="c-name">DesertGulfs.com</td><td class="c-cat"><svg class="ic"><use href="#i-laptop"/></svg>Computers and Internet</td><td class="c-fee"><span class="fee"><svg class="ic"><use href="#i-coins"/></svg>$1240</span></td><td><span class="offer"><svg class="ic"><use href="#i-tag"/></svg>Make Offer</span></td></tr>
      <tr><td class="c-name">DesertGulfs.com</td><td class="c-cat"><svg class="ic"><use href="#i-laptop"/></svg>Computers and Internet</td><td class="c-fee"><span class="fee"><svg class="ic"><use href="#i-coins"/></svg>$1240</span></td><td><span class="offer"><svg class="ic"><use href="#i-tag"/></svg>Make Offer</span></td></tr>
      <tr><td class="c-name">DesertGulfs.com</td><td class="c-cat"><svg class="ic"><use href="#i-laptop"/></svg>Computers and Internet</td><td class="c-fee"><span class="fee"><svg class="ic"><use href="#i-coins"/></svg>$1240</span></td><td><span class="offer"><svg class="ic"><use href="#i-tag"/></svg>Make Offer</span></td></tr>
      <tr><td class="c-name">DesertGulfs.com</td><td class="c-cat"><svg class="ic"><use href="#i-laptop"/></svg>Computers and Internet</td><td class="c-fee"><span class="fee"><svg class="ic"><use href="#i-coins"/></svg>$1240</span></td><td><span class="offer"><svg class="ic"><use href="#i-tag"/></svg>Make Offer</span></td></tr>
      <tr><td class="c-name">DesertGulfs.com</td><td class="c-cat"><svg class="ic"><use href="#i-laptop"/></svg>Computers and Internet</td><td class="c-fee"><span class="fee"><svg class="ic"><use href="#i-coins"/></svg>$1240</span></td><td><span class="offer"><svg class="ic"><use href="#i-tag"/></svg>Make Offer</span></td></tr>
      <tr><td class="c-name">DesertGulfs.com</td><td class="c-cat"><svg class="ic"><use href="#i-laptop"/></svg>Computers and Internet</td><td class="c-fee"><span class="fee"><svg class="ic"><use href="#i-coins"/></svg>$1240</span></td><td><span class="offer"><svg class="ic"><use href="#i-tag"/></svg>Make Offer</span></td></tr>
    </tbody>
  </table>

  <nav class="pager">
    <a href="#">‹</a><a href="#">1</a><a href="#">2</a><a href="#">3</a><a class="on" href="#">4</a><a href="#">5</a><a class="gap">…</a><a href="#">10</a><a href="#">20</a><a href="#">30</a><a href="#">›</a>
  </nav>
</main>

<footer class="footer">
  <div class="col" style="width:430px">
    <h4>About Domain</h4>
    <p>It is a long established fact that a reader will be distracted by the readable content of a page when looking at its layout.</p>
  </div>
  <div class="col" style="width:349px">
    <h4>Domains For Sale</h4>
    <ul><li>yourdomainname.com</li><li>yourdomainname.com</li><li>yourdomainname.com</li></ul>
  </div>
  <div class="col" style="width:421px">
    <h4>Stay Connected With Us</h4>
    <div class="social"><span aria-label="Social link 1"></span><span aria-label="Social link 2"></span><span aria-label="Social link 3"></span><span aria-label="Social link 4"></span><span aria-label="Social link 5"></span></div>
  </div>
</footer>
<p class="copy">© Copyright 2014 - Company name</p>
</body>
</html>
```